Medical equipment business looking for professional, unique business card

We need a business card design for a durable medical equipment company. We are small but would like our cards to express that we are much bigger. We focus on braces (back, knee, wrist, etc) but also do crutches, rollators, wheelchairs- basically medical equipment that gets you going and back in Action. Our colors are blue and green and our logo has an arrow and use of a "spine". We'd like to express professionalism while being unique.

Industry/Entity Type

Medical Equipment

Contact Information for Business Card

Professional feel but unique. Memorable.

Font styles to use
Serif
Sans Serif
Other font styles liked:
• verdana

Requirements
Must have
• card holders cell#, business phone#, fax#, email, website address, business address, logo
Nice to have
• use of medical/healthcare related descriptive words, items, look
Should not have
• the wrong colors or cartoon characters.

```html
<!DOCTYPE html>
<html lang="en">
<head>
<meta charset="utf-8">
<title>Stride Medical – Business Card</title>
<link href="https://fonts.googleapis.com/css2?family=Open+Sans:wght@400;700&display=swap" rel="stylesheet">
<style>
  :root {
    --navy: #0b4870;
    --green: #8dc63f;
    --text-grey: #4a4a4a;
    --rule: #7fa9c4;
    --paper: #ffffff;
    --backdrop: #e9e7e3;
  }
  * { box-sizing: border-box; margin: 0; padding: 0; }
  html, body {
    width: 1200px; height: 987px; overflow: hidden;
    background: var(--backdrop);
    font-family: "Open Sans", Verdana, sans-serif;
  }
  .card {
    position: absolute; width: 615px; height: 351px;
    box-shadow: 0 2px 6px rgba(0,0,0,0.25);
  }
  .card-front { left: 293px; top: 130px; background: var(--paper); overflow: hidden; }
  .card-back { left: 292px; top: 506px; background: var(--green); }

  .brand {
    position: absolute; color: var(--navy); font-weight: 700;
    display: flex; align-items: center; gap: 10px; white-space: nowrap;
  }
  .brand-dot { width: 14px; height: 14px; border-radius: 50%; background: var(--green); }
  .card-front .brand { right: 35px; top: 58px; font-size: 34px; }
  .card-back .brand { left: 0; right: 0; top: 148px; justify-content: center; font-size: 44px; }
  .card-back .brand-dot { background: var(--navy); width: 18px; height: 18px; }

  .holder { position: absolute; left: 33px; top: 128px; }
  .holder-name { font-size: 23px; font-weight: 700; color: var(--navy); line-height: 1.2; }
  .holder-title { font-size: 17px; color: var(--green); line-height: 1.3; }

  .divider {
    position: absolute; left: 33px; top: 207px; width: 547px; height: 1px;
    background: var(--rule);
  }

  .contacts { position: absolute; left: 33px; top: 218px; list-style: none; }
  .contacts li {
    display: flex; align-items: center; gap: 8px;
    font-size: 16.5px; color: var(--text-grey); height: 23.5px;
  }
  .contacts svg { width: 17px; height: 17px; fill: var(--navy); flex: none; }

  .social { position: absolute; right: 35px; top: 236px; display: flex; gap: 6px; }
  .social span { width: 19px; height: 19px; border-radius: 50%; background: var(--navy); }

  .address {
    position: absolute; right: 35px; top: 260px; text-align: right;
    font-size: 16.5px; color: var(--text-grey); line-height: 1.3;
  }

  .bands { position: absolute; left: 0; bottom: 0; width: 615px; height: 35px; }
  .website {
    position: absolute; right: 35px; bottom: 6px;
    font-size: 16.5px; color: var(--navy); letter-spacing: 0.5px;
  }
</style>
</head>
<body>

<section class="card card-front">
  <div class="brand"><span class="brand-dot"></span>Stride Medical</div>

  <div class="holder">
    <p class="holder-name">Daniel Reyes</p>
    <p class="holder-title">CEO/Founder</p>
  </div>

  <div class="divider"></div>

  <ul class="contacts">
    <li>
      <svg viewBox="0 0 24 24" aria-hidden="true"><path d="M6.6 10.8a15.1 15.1 0 0 0 6.6 6.6l2.2-2.2c.3-.3.7-.4 1-.2 1.1.4 2.3.6 3.6.6.6 0 1 .4 1 1V20c0 .6-.4 1-1 1A17 17 0 0 1 3 4c0-.6.4-1 1-1h3.5c.6 0 1 .4 1 1 0 1.3.2 2.5.6 3.6.1.3 0 .7-.2 1z"/></svg>
      555 210 4470
    </li>
    <li>
      <svg viewBox="0 0 24 24" aria-hidden="true"><path d="M7 1h10a2 2 0 0 1 2 2v18a2 2 0 0 1-2 2H7a2 2 0 0 1-2-2V3a2 2 0 0 1 2-2zm0 3v14h10V4zm5 15.5a1 1 0 1 0 0 2 1 1 0 0 0 0-2z"/></svg>
      555 318 2096
    </li>
    <li>
      <svg viewBox="0 0 24 24" aria-hidden="true"><path d="M6 2h10l2 2v5H6zM3 10h18a1 1 0 0 1 1 1v8a1 1 0 0 1-1 1H3a1 1 0 0 1-1-1v-8a1 1 0 0 1 1-1zm3 5v4h12v-4z"/></svg>
      555 604 7712
    </li>
    <li>
      <svg viewBox="0 0 24 24" aria-hidden="true"><path d="M2 5h20v14H2zm2 2v.5l8 5.5 8-5.5V7zm0 3v7h16v-7l-8 5.5z"/></svg>
      hello@stridemed.com
    </li>
  </ul>

  <div class="social" aria-label="Social media">
    <span></span><span></span><span></span><span></span>
  </div>

  <p class="address">1420 Harbor View Road<br>Fairview, Oregon 97024</p>

  <svg class="bands" viewBox="0 0 615 35" preserveAspectRatio="none" aria-hidden="true">
    <polygon points="0,20 374,20 363,35 0,35" fill="var(--navy)"/>
    <polygon points="387,0 615,0 615,35 363,35" fill="var(--green)"/>
  </svg>
  <p class="website">www.stridemed.com</p>
</section>

<section class="card card-back">
  <div class="brand"><span class="brand-dot"></span>Stride Medical</div>
</section>

</body>
</html>
```